medical practice needs a printed banner design

we need a printed banner for a new pain management medical practice in Las Vegas. The name of the practice is "Marlowe Pain Relief Center".
39" x 80" vertical banner
the look should be modern, clean, professional and in line with design of website. Please visit the website for more information regarding the practice.

Target Market(s)

age typically 40+, patients with back pain, joint pain

Industry/Entity Type

Doctor

Requirements
Must have
• our logo (attached file)
• phone number: (702) 555-0187
• website address: marlowepaincareclinic.example
• Hablamos EspaƱol
Nice to have
• slogan: Live Better (banner does not necessarily need to include slogan, but would be preferred)
• maybe a photo of spine, or photo depicting back pain, or active lifestyle
Should not have
• please do not include physical address location as we will be relocating
• * in addition, we hope the banner is not to be misconstrued as a chiropractic
• practice

```html
<!DOCTYPE html>
<html lang="en">
<head>
<meta charset="utf-8">
<title>Marlowe Pain Relief Center – Roll-up Banner</title>
<link rel="stylesheet" href="https://fonts.googleapis.com/css2?family=Montserrat:wght@600;700&family=Open+Sans:wght@400;600&display=swap">
<style>
  :root {
    --navy: #26365c;
    --navy-deep: #1d2a4a;
    --teal: #3aa7ae;
    --teal-band: #5dbcc0;
    --ink: #2a2f3a;
    --paper: #ffffff;
    --mist: #eef0f2;
    --muscle: #b5534a;
    --muscle-light: #d8a79c;
  }
  * { margin: 0; padding: 0; box-sizing: border-box; }
  html, body { width: 889px; height: 1200px; overflow: hidden; background: var(--paper); }
  .banner {
    position: relative;
    width: 889px;
    height: 1200px;
    display: flex;
    flex-direction: column;
    background: var(--paper);
    font-family: "Open Sans", Arial, sans-serif;
  }
  .web-bar {
    height: 88px;
    background: var(--navy);
    border-bottom: 6px solid var(--teal);
    display: flex;
    align-items: center;
    justify-content: center;
    color: var(--paper);
    font-size: 30px;
    letter-spacing: 0.5px;
  }
  .brand {
    height: 250px;
    display: flex;
    flex-direction: column;
    align-items: center;
    justify-content: center;
    gap: 14px;
    color: var(--navy);
    font-family: "Montserrat", Arial, sans-serif;
    font-weight: 600;
    text-align: center;
  }
  .brand-mark {
    width: 58px;
    height: 58px;
    background: var(--teal);
  }
  .brand-name {
    font-size: 74px;
    letter-spacing: 6px;
    line-height: 1;
    text-transform: uppercase;
  }
  .brand-sub {
    font-size: 30px;
    letter-spacing: 9px;
    line-height: 1;
    text-transform: uppercase;
  }
  .hero-art {
    flex: 1;
    margin: 0 80px;
    background: radial-gradient(ellipse at 50% 50%, var(--muscle-light) 0%, #ecd9d3 35%, var(--mist) 62%, var(--paper) 85%);
  }
  .tagline {
    height: 86px;
    display: flex;
    align-items: center;
    justify-content: center;
    font-size: 40px;
    color: var(--ink);
  }
  .contact-band {
    height: 196px;
    background: var(--teal-band);
    display: flex;
    flex-direction: column;
    align-items: center;
    justify-content: center;
    gap: 12px;
    text-align: center;
  }
  .insurance { color: var(--paper); font-size: 24px; }
  .call { color: var(--navy-deep); font-size: 30px; font-weight: 600; }
  .spanish { color: var(--paper); font-size: 28px; font-weight: 600; }
  .base-strip { height: 30px; background: var(--navy); }
</style>
</head>
<body>
  <main class="banner">
    <header class="web-bar">www.marlowepaincareclinic.example</header>

    <section class="brand">
      <div class="brand-mark"></div>
      <div class="brand-name">Marlowe</div>
      <div class="brand-sub">Pain Relief Center</div>
    </section>

    <div class="hero-art" role="img" aria-label="Anatomical muscle illustration of an athlete in a discus-throwing pose"></div>

    <p class="tagline">Specialized in Pain Treatment</p>

    <section class="contact-band">
      <p class="insurance">Accepting Most Insurances</p>
      <p class="call">FOR MORE INFORMATION CALL (702) 555-0187</p>
      <p class="spanish">Hablamos Español</p>
    </section>
    <div class="base-strip"></div>
  </main>
</body>
</html>
```